Banner für Immobilienmakler
Zielgruppe
Immobilienmakler, Immobilienverkauf mit Herz,
Aufgabenstellung
Verkauf von Häusern und Wohnungen, der Banner soll an einen Balkon oder einen Zaun angebracht werden mit dem Hinweis, dass das Haus Zu verkaufen ist.
Maße ca. 76 x 244cm
Es darf gerne frech und modern sein mit einem witzigen einladenden Spruch sein, sollte aber auch ansonsten zu meinem chicen Style passen (siehe Homepage www.kranichhausverkauf.de) es soll sich abheben von anderen langweiligen Bannern.
Ggf soll die Plane auch noch an einem Tennisplatz angebracht werden

```html
<!DOCTYPE html>
<html lang="en">
<head>
<meta charset="utf-8">
<title>House for Sale Banner</title>
<link href="https://fonts.googleapis.com/css2?family=Bebas+Neue&family=Poppins:wght@400;500&display=swap" rel="stylesheet">
<style>
  :root {
    --backdrop: #d4d4d4;
    --gold: #bc9b63;
    --sand: #f2ebe4;
    --white: #ffffff;
    --ink: #111111;
  }
  * { margin: 0; padding: 0; box-sizing: border-box; }
  html, body { width: 1200px; height: 1200px; overflow: hidden; background: var(--backdrop); }
  .banner {
    position: absolute; left: 35px; top: 420px;
    width: 1130px; height: 359px;
    background: var(--white); overflow: hidden;
    font-family: "Poppins", sans-serif;
  }
  .brand {
    position: absolute; left: 26px; top: 48px;
    display: flex; align-items: center; gap: 8px;
    color: var(--gold); font-size: 13px; font-weight: 500; letter-spacing: 0.5px;
  }
  .brand-dot {
    width: 22px; height: 22px; border: 2px solid var(--gold); border-radius: 50%;
  }
  .headline-band {
    position: absolute; left: 0; top: 133px; width: 640px; height: 87px;
    background: var(--sand);
  }
  .headline {
    position: absolute; left: 44px; top: 136px;
    font-family: "Bebas Neue", sans-serif; font-size: 90px; line-height: 84px;
    color: var(--gold); letter-spacing: 0.5px; white-space: nowrap;
  }
  .scene { position: absolute; left: 0; top: 0; }
  .contact { position: absolute; left: 45px; top: 262px; display: flex; gap: 9px; }
  .contact-icon { width: 47px; height: 58px; }
  .contact-text { color: var(--ink); }
  .contact-lead { font-size: 13px; line-height: 16px; margin-top: -2px; }
  .contact-phone { font-size: 20.5px; line-height: 25px; }
  .thumb {
    position: absolute; top: 196px; width: 117px; height: 115px;
    border: 5px solid var(--white); border-bottom: none;
  }
  .thumb-block { left: 816px; border-top-left-radius: 30px; background: linear-gradient(170deg, #8fb4dc 0%, #7a6f6a 45%, #9a6a52 75%, #6f6f6f 100%); }
  .thumb-villa { left: 941px; border-top-right-radius: 30px; background: linear-gradient(180deg, #3f72c8 0%, #5c86cf 40%, #e2c877 62%, #5a6f9c 85%, #4a4a4a 100%); }
  .bottom-bar { position: absolute; left: 0; bottom: 0; width: 1130px; height: 15px; background: var(--gold); }
  .email-tab { position: absolute; left: 764px; top: 317px; }
  .email {
    position: absolute; right: 14px; top: 318px; height: 30px;
    display: flex; align-items: center; gap: 9px;
    color: var(--white); font-size: 19px; white-space: nowrap;
  }
  .email-icon { width: 25px; height: 25px; flex: none; }
</style>
</head>
<body>
<div class="banner">
  <div class="brand"><span class="brand-dot"></span><span>Kranich Immobilien</span></div>

  <div class="headline-band"></div>

  <svg class="scene" width="1130" height="359" viewBox="0 0 1130 359">
    <defs>
      <linearGradient id="roomTone" x1="0" y1="0" x2="1" y2="0.3">
        <stop offset="0" stop-color="#7b7a72"/>
        <stop offset="0.22" stop-color="#c9d3c9"/>
        <stop offset="0.35" stop-color="#9aa38a"/>
        <stop offset="0.5" stop-color="#6a6a68"/>
        <stop offset="0.75" stop-color="#d9d6d0"/>
        <stop offset="1" stop-color="#cbc4bb"/>
      </linearGradient>
    </defs>
    <path d="M511 0 C511 150 590 263 760 263 L1130 263 L1130 0 Z" fill="var(--gold)"/>
    <g role="img" aria-label="Photo of a bright empty living room with a large window overlooking the town">
      <path d="M520 0 C520 145 598 255 760 255 L1130 255 L1130 0 Z" fill="url(#roomTone)"/>
    </g>
  </svg>

  <div class="headline">HOUSE FOR SALE</div>

  <div class="thumb thumb-block" role="img" aria-label="Photo of a brick apartment building with balconies"></div>
  <div class="thumb thumb-villa" role="img" aria-label="Photo of a yellow detached house with a garage under blue sky"></div>

  <div class="contact">
    <svg class="contact-icon" viewBox="0 0 47 58">
      <rect x="0" y="0" width="47" height="52" rx="4" fill="var(--gold)"/>
      <rect x="4" y="54" width="43" height="3" fill="var(--gold)"/>
      <path d="M12 14 l5 -3 l5 8 l-3 3 c2 5 5 8 9 10 l3 -3 l8 5 l-3 5 c-12 1 -25 -12 -24 -25 z" fill="var(--white)"/>
    </svg>
    <div class="contact-text">
      <p class="contact-lead">More information call us</p>
      <p class="contact-phone">0170 – 123 45 67</p>
      <p class="contact-phone">02241 – 80 80 321</p>
    </div>
  </div>

  <svg class="email-tab" width="366" height="42" viewBox="0 0 366 42">
    <path d="M0 27 C8 10 18 0 45 0 L366 0 L366 42 L0 42 Z" fill="var(--gold)"/>
  </svg>
  <div class="bottom-bar"></div>

  <div class="email">
    <svg class="email-icon" viewBox="0 0 26 26">
      <circle cx="13" cy="13" r="13" fill="var(--white)"/>
      <rect x="6" y="8.5" width="14" height="9" fill="var(--gold)"/>
      <path d="M6 8.5 L13 14 L20 8.5" fill="none" stroke="var(--white)" stroke-width="1"/>
    </svg>
    <span>info@kranichhausverkauf.de</span>
  </div>
</div>
</body>
</html>
```